Design some Business Cards for Wendlocks

Hi everyone,

We are in need of a new business card design. Artwork is to be in 3 colours - white, black and orange. I have attached a photo of the colours I would like. The logo is attached as an EPS & PDF. Size of the card is to be slimline 90x45mm landscape.

There is an opportunity for ongoing work for the winning freelancer.

We will require on the card:
Person's Name
Company Position
Mobile/Cell Phone Number
Office Phone Number
Email Address
Website
Street Address

```html
<!DOCTYPE html>
<html lang="en">
<head>
<meta charset="utf-8">
<title>Wendlocks Business Cards</title>
<link href="https://fonts.googleapis.com/css2?family=Open+Sans:wght@400;600;700&display=swap" rel="stylesheet">
<style>
  :root {
    --orange: #f47321;
    --white: #ffffff;
    --ink: #333333;
    --backdrop: #d9d9d9;
  }
  * { box-sizing: border-box; margin: 0; padding: 0; }
  html, body {
    width: 1200px; height: 960px; overflow: hidden;
    background: var(--backdrop);
    font-family: "Open Sans", Arial, sans-serif;
  }
  .canvas {
    position: relative; width: 1200px; height: 960px;
  }
  .card {
    position: absolute; left: 240px; width: 720px; height: 400px;
    box-shadow: 0 6px 18px rgba(0,0,0,0.18);
    overflow: hidden;
  }
  .card--front { top: 60px; background: var(--orange); }
  .card--back { top: 500px; background: var(--white); }

  .brand-name {
    position: absolute; left: 0; right: 0; text-align: center;
    font-weight: 700; letter-spacing: 1px;
  }
  .card--front .brand-name {
    top: 150px; font-size: 78px; color: var(--white); line-height: 1;
  }
  .card--back .brand-name {
    top: 70px; font-size: 66px; color: var(--orange); line-height: 1;
  }

  .holder {
    position: absolute; top: 205px; right: 372px; text-align: right;
  }
  .holder__name {
    font-size: 26px; color: var(--orange); font-weight: 400; line-height: 1.1;
  }
  .holder__role {
    font-size: 13px; color: var(--ink); margin-top: 2px;
  }
  .address {
    position: absolute; top: 265px; right: 372px; text-align: right;
    font-size: 17px; color: var(--ink); line-height: 1.3;
  }

  .contacts {
    position: absolute; top: 238px; left: 372px; list-style: none;
  }
  .contacts li {
    display: flex; align-items: center; gap: 10px;
    font-size: 17px; color: var(--ink); line-height: 1.3; height: 23px;
  }
  .contacts svg { width: 15px; height: 15px; fill: var(--orange); flex: none; }

  .band {
    position: absolute; left: 0; right: 0; bottom: 0; height: 28px;
    background: var(--orange);
  }
</style>
</head>
<body>
<div class="canvas">

  <section class="card card--front" aria-label="Card front">
    <div class="brand-name">Wendlocks</div>
  </section>

  <section class="card card--back" aria-label="Card back">
    <div class="brand-name">Wendlocks</div>

    <div class="holder">
      <div class="holder__name">Mara Lindqvist</div>
      <div class="holder__role">Manager</div>
    </div>

    <div class="address">
      PO BOX 5180, 4020 Linz,<br>Austria 5180
    </div>

    <ul class="contacts">
      <li>
        <svg viewBox="0 0 24 24" aria-hidden="true"><path d="M6.6 10.8a15.1 15.1 0 0 0 6.6 6.6l2.2-2.2c.3-.3.7-.4 1-.2 1.1.4 2.3.6 3.6.6.6 0 1 .4 1 1V20c0 .6-.4 1-1 1A17 17 0 0 1 3 4c0-.6.4-1 1-1h3.5c.6 0 1 .4 1 1 0 1.3.2 2.5.6 3.6.1.3 0 .7-.2 1z"/></svg>
        144 308 527
      </li>
      <li>
        <svg viewBox="0 0 24 24" aria-hidden="true"><path d="M7 2h10a2 2 0 0 1 2 2v16a2 2 0 0 1-2 2H7a2 2 0 0 1-2-2V4a2 2 0 0 1 2-2zm0 3v13h10V5zm5 14.2a1 1 0 1 0 0 2 1 1 0 0 0 0-2z"/></svg>
        144 308 528
      </li>
      <li>
        <svg viewBox="0 0 24 24" aria-hidden="true"><path d="M7 2h10v5H7zM4 8h16a2 2 0 0 1 2 2v7h-4v5H6v-5H2v-7a2 2 0 0 1 2-2zm4 7v5h8v-5z"/></svg>
        144 308 529
      </li>
      <li>
        <svg viewBox="0 0 24 24" aria-hidden="true"><path d="M2 5h20v14H2zm2 2v.4l8 5.3 8-5.3V7zm0 2.8V17h16V9.8l-8 5.3z"/></svg>
        hello@wendlocks.com
      </li>
      <li>
        <svg viewBox="0 0 24 24" aria-hidden="true"><path d="M12 2a10 10 0 1 0 0 20 10 10 0 0 0 0-20zm6.9 9h-3a15 15 0 0 0-1.3-5.8A8 8 0 0 1 18.9 11zM12 4.1c.9 1.2 1.8 3.6 1.9 6.9h-3.8c.1-3.3 1-5.7 1.9-6.9zM9.4 5.2A15 15 0 0 0 8.1 11h-3a8 8 0 0 1 4.3-5.8zM5.1 13h3a15 15 0 0 0 1.3 5.8A8 8 0 0 1 5.1 13zm6.9 6.9c-.9-1.2-1.8-3.6-1.9-6.9h3.8c-.1 3.3-1 5.7-1.9 6.9zm2.6-1.1a15 15 0 0 0 1.3-5.8h3a8 8 0 0 1-4.3 5.8z"/></svg>
        www.wendlocks.com
      </li>
    </ul>

    <div class="band"></div>
  </section>

</div>
</body>
</html>
```